Halvex Therapeutics is a biotech company that needs a powerpoint theme.

We need a powerpoint theme with several different slide templates we could use for presentation of data or research ideas. Our logo is attached. We picked "Halvex" as our company name because we use epigenome editing tools to fine-tune gene expression for therapeutic purposes. Our logo color is a seafoam green, and we would like to see this color along with other colors that could complement it well. Keywords: genetics, biotech, cells, human therapies,

```html
<!DOCTYPE html>
<html lang="en">
<head>
<meta charset="UTF-8">
<title>Halvex Therapeutics – Content Slide</title>
<link rel="stylesheet" href="https://fonts.googleapis.com/css2?family=Open+Sans:wght@300;400;600&display=swap">
<style>
  :root {
    --slate: #353746;
    --seafoam: #1fc1ad;
    --coral: #f6836f;
    --cream: #efe2d8;
    --paper: #f4f4f5;
    --ink: #3a3a3f;
    --body-text: #eef0f2;
  }
  html, body {
    margin: 0;
    padding: 0;
    overflow: hidden;
    background: var(--slate);
  }
  .slide {
    position: relative;
    width: 1200px;
    height: 675px;
    overflow: hidden;
    background: var(--slate);
    font-family: "Open Sans", sans-serif;
  }
  .slide-title {
    position: absolute;
    left: 92px;
    top: 38px;
    margin: 0;
    font-weight: 300;
    font-size: 42px;
    line-height: 56px;
    color: var(--seafoam);
  }
  .title-rule {
    position: absolute;
    left: 75px;
    top: 95px;
    width: 1051px;
    height: 2px;
    background: var(--seafoam);
  }
  .body-copy {
    position: absolute;
    left: 92px;
    top: 162px;
    width: 478px;
    margin: 0;
    font-size: 17.5px;
    line-height: 26.5px;
    font-weight: 400;
    color: var(--body-text);
  }
  .illustration {
    position: absolute;
    left: 752px;
    top: 140px;
    width: 354px;
    height: 408px;
    border-radius: 40px;
    background:
      radial-gradient(circle at 35% 30%, rgba(31,193,173,0.45), transparent 55%),
      radial-gradient(circle at 75% 35%, rgba(246,131,111,0.40), transparent 50%),
      radial-gradient(circle at 50% 78%, rgba(239,226,216,0.35), transparent 55%),
      rgba(255,255,255,0.03);
  }
  .footer-wave {
    position: absolute;
    left: 0;
    top: 0;
    width: 1200px;
    height: 675px;
  }
  .brand {
    position: absolute;
    left: 201px;
    top: 607px;
    display: flex;
    align-items: center;
    gap: 14px;
  }
  .brand-dot {
    width: 50px;
    height: 50px;
    border-radius: 50%;
    background: var(--seafoam);
  }
  .brand-name {
    font-family: "Open Sans", sans-serif;
    font-weight: 400;
    font-size: 22px;
    letter-spacing: 1px;
    color: var(--ink);
  }
  .page-number {
    position: absolute;
    right: 56px;
    top: 627px;
    font-size: 25px;
    font-weight: 400;
    color: var(--ink);
  }
</style>
</head>
<body>
<div class="slide">
  <h1 class="slide-title">Add your title here</h1>
  <div class="title-rule"></div>

  <p class="body-copy">We need a powerpoint theme with several different slide templates we could use for presentation of data or research ideas. Our logo is attached. We picked "Halvex" as our company name because we use epigenome editing tools to fine-tune gene expression for therapeutic purposes. Our logo color is a seafoam green, and we would like to see this color along with other colors that could complement it well. Keywords: genetics, biotech, cells, human therapies,</p>

  <div class="illustration" role="img" aria-label="Illustration of three DNA double helices in seafoam, coral and cream with scattered dots"></div>

  <svg class="footer-wave" viewBox="0 0 1200 675" aria-hidden="false">
    <path d="M0 622 C150 598 300 578 480 600 C650 622 800 652 950 632 C1050 618 1130 584 1200 552 L1200 675 L0 675 Z" fill="var(--paper)"/>
    <g role="img" aria-label="Decorative DNA strand pattern running along the wave edge">
      <path d="M0 622 C150 598 300 578 480 600 C650 622 800 652 950 632 C1050 618 1130 584 1200 552" fill="none" stroke="var(--seafoam)" stroke-width="7" stroke-opacity="0.55"/>
      <path d="M0 630 C150 640 300 625 480 618 C650 628 800 650 950 642" fill="none" stroke="var(--seafoam)" stroke-width="6" stroke-opacity="0.35"/>
    </g>
  </svg>

  <div class="brand">
    <span class="brand-dot"></span>
    <span class="brand-name">Halvex Therapeutics</span>
  </div>

  <div class="page-number">30</div>
</div>
</body>
</html>
```